i need a business card for a plumbing company in california

we are a drain cleaning , maintenance plumbing company who is starting new marketing campaign for a tatrench-less pipe installation department .

Target Market(s)

the professional who appreciates time and quality workmanship.

Industry/Entity Type

Plumbing

Colors
0655a3
ec1f27

Requirements
Must have
• the second logo needs to be included
Nice to have
• a focus on the services offered
Should not have
• any underlined words on the brief

```html
<!DOCTYPE html>
<html lang="en">
<head>
<meta charset="utf-8">
<title>Crestline Pipe Works – Business Card</title>
<link href="https://fonts.googleapis.com/css2?family=Exo+2:ital,wght@0,500;0,600;1,300;1,600&family=PT+Sans:ital,wght@0,400;1,400&display=swap" rel="stylesheet">
<style>
  :root {
    --brand-blue: #0655a3;
    --brand-red: #ec1f27;
    --charcoal: #343537;
    --paper: #f6f6f6;
    --ink: #2b2b2b;
    --mark-grey: #6d6e70;
    --stage: #e9e9eb;
    --placeholder: #d9e3ee;
  }
  * { box-sizing: border-box; margin: 0; padding: 0; }
  html, body { width: 725px; height: 1200px; overflow: hidden; }
  body {
    background: var(--stage);
    font-family: "PT Sans", sans-serif;
    position: relative;
  }
  .card {
    position: absolute;
    left: 77px;
    width: 570px;
    height: 334px;
    background: var(--paper);
    overflow: hidden;
    box-shadow: 0 14px 22px rgba(0,0,0,0.22);
  }
  .card--front { top: 220px; background: var(--charcoal); }
  .card--back { top: 650px; }

  .card__art { position: absolute; inset: 0; }

  .wordmark {
    position: absolute;
    display: flex;
    align-items: center;
    gap: 10px;
    font-family: "Exo 2", sans-serif;
    font-weight: 600;
    color: var(--mark-grey);
    line-height: 0.95;
  }
  .wordmark__dot {
    width: 22px; height: 22px;
    border-radius: 50%;
    background: var(--brand-red);
    flex: none;
  }
  .card--front .wordmark { left: 30px; top: 142px; font-size: 28px; }
  .card--back .wordmark { left: 340px; top: 38px; font-size: 25px; }

  .blue-tab {
    position: absolute;
    right: 0; top: 96px;
    width: 20px; height: 140px;
    background: var(--brand-blue);
    border-radius: 6px 0 0 6px;
  }
  .tagline {
    position: absolute;
    left: 300px; top: 116px;
    width: 240px;
    text-align: center;
    font-family: "Exo 2", sans-serif;
    font-style: italic;
  }
  .tagline__lead { display: block; color: #fff; font-weight: 300; font-size: 27px; }
  .tagline__example { display: block; color: var(--brand-red); font-weight: 600; font-size: 40px; line-height: 1.05; }
  .services {
    position: absolute;
    left: 255px; top: 251px;
    width: 290px;
    text-align: center;
    color: #f1f1f1;
    font-size: 12.5px;
    line-height: 1.42;
  }
  .services em { margin-left: 4px; }

  .side-bar {
    position: absolute; left: 0; top: 0;
    width: 22px; height: 100%;
    background: var(--brand-blue);
  }
  .person { position: absolute; left: 38px; top: 42px; }
  .person__name {
    font-family: "Exo 2", sans-serif;
    font-weight: 600;
    font-size: 29px;
    color: var(--brand-red);
    line-height: 1;
  }
  .person__role { font-style: italic; font-size: 18px; color: #555; }

  .contacts { position: absolute; left: 22px; top: 124px; list-style: none; }
  .contacts li {
    display: flex; align-items: center;
    height: 23px; margin-bottom: 8.5px;
    font-size: 14.5px; color: var(--ink);
  }
  .contacts__icon {
    width: 36px; height: 23px;
    background: var(--brand-red);
    border-radius: 0 5px 5px 0;
    display: flex; align-items: center; justify-content: center;
    margin-right: 10px;
  }
  .contacts__icon svg { width: 13px; height: 13px; }

  .emblem-placeholder {
    position: absolute; left: 392px; top: 118px;
    width: 100px; height: 100px; border-radius: 50%;
    background: var(--placeholder);
  }

  .social-band {
    position: absolute; left: 22px; top: 236px;
    width: 410px; height: 35px;
    background: var(--brand-blue);
    border-radius: 0 18px 18px 0;
    display: flex; align-items: center;
    padding-left: 14px;
    color: #fff; font-size: 13.5px;
  }
  .social-band__divider { width: 1px; height: 20px; background: rgba(255,255,255,0.7); margin: 0 12px; }
  .social-band__dot {
    width: 24px; height: 24px; border-radius: 50%;
    background: #fff; margin-right: 11px;
  }
  .social-band__square { width: 18px; height: 24px; background: #fff; border-radius: 3px; }

  .channel {
    position: absolute; left: 34px; top: 284px;
    display: flex; align-items: center; gap: 12px;
    font-size: 13.5px; color: var(--ink);
  }
  .channel__square { width: 18px; height: 18px; background: var(--ink); border-radius: 3px; }
</style>
</head>
<body>

  <section class="card card--front" aria-label="Card front">
    <svg class="card__art" viewBox="0 0 570 334" aria-hidden="true">
      <path d="M0 0 L244 0 C312 62 300 230 214 334 L0 334 Z" fill="var(--brand-red)"/>
      <path d="M0 0 L228 0 C300 62 290 230 209 334 L0 334 Z" fill="var(--brand-blue)"/>
      <path d="M0 0 L200 0 C282 62 282 230 205 334 L0 334 Z" fill="var(--paper)"/>
    </svg>
    <div class="blue-tab"></div>
    <div class="wordmark"><span>Crestline<br>Pipe Works</span><span class="wordmark__dot"></span></div>
    <h1 class="tagline">
      <span class="tagline__lead">Lead by</span>
      <span class="tagline__example">Example…</span>
    </h1>
    <p class="services">
      Virgin Trench-Less Installs &amp; Replacements -<br>
      Pipe Bursting &amp; Pipe Piercing Install,<br>
      Replace, Pipe Enlargement <em>PULL &amp; GO</em>
    </p>
  </section>

  <section class="card card--back" aria-label="Card back">
    <div class="side-bar"></div>
    <div class="person">
      <h2 class="person__name">Marco Delgado</h2>
      <p class="person__role">Owner</p>
    </div>
    <div class="wordmark"><span>Crestline<br>Pipe Works</span><span class="wordmark__dot"></span></div>

    <ul class="contacts">
      <li><span class="contacts__icon">
        <svg viewBox="0 0 16 16"><path d="M4 1 L6.5 4.5 L5 6.5 C6 8.5 7.5 10 9.5 11 L11.5 9.5 L15 12 L13 15 C7 14 2 9 1 3 Z" fill="#fff"/></svg>
      </span>5550142290</li>
      <li><span class="contacts__icon">
        <svg viewBox="0 0 16 16"><rect x="1" y="3" width="14" height="10" fill="#fff"/><path d="M1 3 L8 9 L15 3" fill="none" stroke="var(--brand-red)" stroke-width="1.4"/></svg>
      </span>info@CrestlinePipeWorks.com</li>
      <li><span class="contacts__icon">
        <svg viewBox="0 0 16 16" fill="none" stroke="#fff" stroke-width="1.3"><circle cx="8" cy="8" r="6.5"/><ellipse cx="8" cy="8" rx="3" ry="6.5"/><path d="M1.5 8 H14.5 M2.5 4.5 H13.5 M2.5 11.5 H13.5"/></svg>
      </span>www.CrestlinePipeWorks.com</li>
    </ul>

    <div class="emblem-placeholder" role="img" aria-label="Placeholder for the company's round service emblem"></div>

    <div class="social-band">
      <span>/CrestlinePipeWorks</span>
      <span class="social-band__divider"></span>
      <span class="social-band__dot"></span>
      <span class="social-band__dot"></span>
      <span class="social-band__dot"></span>
      <span class="social-band__dot"></span>
      <span class="social-band__square"></span>
    </div>

    <div class="channel"><span class="channel__square"></span><span>CrestlinePipeWorks</span></div>
  </section>

</body>
</html>
```